Kivo4 Website design (Need help to re-design our website)

We need someone to help us re-design our website and launch it. All contents for the website are ready. (Website: https://www.kivo4.com.au/)

-Rearrange categories:
1. Heat Pumps (Link to PALOX site: https://palox.com.au/)
2. Solar (Under the Solar category; remove solar panels, solar inverters, and solar batteries)
3. LED
4. Capability Statement
5. Service and Support
6. Contact us

Home page - redesign but the free quote will stay.

NOTE:
-Try using professional fonts (Example: Helvetica, etc.)
-Try to play with colours related to sustainability, eco-friendliness, solar, energy, and energy efficiency.
-The website's Footer should be readable and use light colour.

Target Market(s)

Residentials & commercial buildings

Industry/Entity Type

SOLAR ENERGY PROVIDER

Coding

Coded - Design and coding required

Colors

Designer to choose colors to be used in the design.

Requirements
Nice to have
• Effects/transition on the words/copy/images.

```html
<!DOCTYPE html>
<html lang="en">
<head>
<meta charset="utf-8">
<title>Kivo4 — Next Generation Energy Saving Products</title>
<link rel="stylesheet" href="https://fonts.googleapis.com/css2?family=Archivo:wght@600;700;800&family=DM+Sans:wght@400;500;700&display=swap">
<style>
:root{
  --blue:#2a44a5;
  --blue-deep:#22398f;
  --green:#2f8a3b;
  --green-light:#6cb33f;
  --label:#6aae35;
  --text:#4a4f5c;
  --muted:#6b7080;
  --line:#e3e6ee;
  --white:#ffffff;
  --sky:#dfe8f3;
}
*{margin:0;padding:0;box-sizing:border-box}
html,body{width:1200px;height:3672px;overflow:hidden}
body{position:relative;background:var(--white);font-family:"DM Sans",sans-serif;color:var(--text)}
.abs{position:absolute}
.head{font-family:"Archivo",sans-serif;font-weight:700;color:var(--blue);text-transform:uppercase;line-height:1.08;letter-spacing:-.4px}
.label{font-family:"DM Sans",sans-serif;font-weight:700;color:var(--label);font-size:12px}
.btn{position:absolute;display:flex;align-items:center;justify-content:center;background:var(--green);color:var(--white);font-weight:700;font-size:11.5px;border-radius:3px;text-decoration:none}
.photo{position:absolute}

/* top bar */
.topbar{left:0;top:0;width:1200px;height:26px;background:var(--blue);color:var(--white);font-size:10px;display:flex;align-items:center;justify-content:center}
.topbar u{font-weight:700}

/* header */
.logo{left:121px;top:56px;display:flex;align-items:center;gap:8px;font-family:"Archivo",sans-serif;font-weight:700;font-size:30px;color:var(--blue)}
.logo i{width:14px;height:14px;border-radius:50%;background:var(--green-light);display:block}
.nav{left:495px;top:53px;display:flex;gap:24px;font-size:11px;font-weight:700;color:var(--blue)}
.nav-cta{left:926px;top:46px;width:89px;height:28px;background:var(--green-light);font-size:11px}
.icon-search{left:1028px;top:53px}
.icon-menu{left:1058px;top:53px}

/* hero */
.hero-bg{left:0;top:28px;width:1200px;height:1222px;background:linear-gradient(180deg,#fff 0%,#f4f6f9 28%,#c9d0c6 45%,#aab6a0 55%,#c8d2c4 70%,#f0f3f6 88%,#fff 100%)}
.hero-panel{left:600px;top:93px;width:477px;height:580px;background:linear-gradient(160deg,#dbe4ec 0%,#6f8c6a 35%,#4c6a8a 60%,#3b5a3a 100%);clip-path:polygon(0 5%,100% 0,100% 100%,0 95%)}
.hero-label{left:121px;top:222px}
.hero-title{left:121px;top:242px;font-size:46px;width:470px;line-height:1.06}
.hero-copy{left:121px;top:400px;width:430px;font-size:11.5px;line-height:20px}
.hero-btn{left:121px;top:479px;width:150px;height:37px}

/* about */
.about-rect{left:315px;top:869px;width:325px;height:300px;background:linear-gradient(180deg,#8fb3d9 0%,#c9d6e3 35%,#3e5b86 65%,#556b3a 100%)}
.about-circle{left:125px;top:724px;width:362px;height:362px;border-radius:50%;border:4px solid var(--white);background:linear-gradient(170deg,#2b86e0 0%,#56aef0 45%,#2c4a8a 75%,#1e2f5a 100%)}
.about-label{left:691px;top:787px}
.about-title{left:691px;top:804px;font-size:34px;width:420px}
.about-lead{left:691px;top:891px;width:390px;font-size:14.5px;font-weight:700;color:#3a3f4c;line-height:20px}
.about-copy{left:691px;top:948px;width:395px;font-size:11.5px;line-height:20px}
.about-copy p+p{margin-top:20px}
.about-btn{left:691px;top:1097px;width:150px;height:37px}

/* quote */
.quote{left:121px;top:1230px;width:956px;height:380px;background:var(--blue)}
.quote-label{left:0;top:48px;width:956px;text-align:center;font-size:12px;font-weight:700;color:var(--white)}
.quote-title{left:0;top:68px;width:956px;text-align:center;font-size:34px;color:var(--white);line-height:1.15}
.field{position:absolute;width:226px;height:37px;border:1px solid rgba(255,255,255,.7);border-radius:3px;color:var(--white);font-size:9.5px;padding:0 12px;display:flex;align-items:center;justify-content:space-between}
.field svg{flex:none}
.submit{left:128px;top:269px;width:701px;height:37px;background:var(--green-light);font-size:11.5px}
.quote-terms{left:0;top:318px;width:956px;text-align:center;color:var(--white);font-size:9.5px}

/* products */
.section-label{width:1200px;left:0;text-align:center}
.prod-title{left:0;top:1690px;width:1200px;text-align:center;font-size:34px;line-height:1.15}
.prod-sub{left:0;top:1777px;width:1200px;text-align:center;font-size:11.5px;color:var(--muted)}
.prod-bg{left:0;top:2160px;width:1200px;height:360px;background:linear-gradient(180deg,#fff 0%,#c7d1d9 35%,#8b9aa3 55%,#d8dfe5 80%,#fff 100%)}
.card{position:absolute;top:1820px;width:306px;height:420px;background:var(--white);box-shadow:0 6px 24px rgba(30,40,70,.08)}
.card-img{position:absolute;left:7px;top:8px;width:292px;height:225px;clip-path:polygon(0 12%,100% 0,100% 100%,0 100%)}
.card-icon{position:absolute;left:129px;top:208px;width:48px;height:48px;border-radius:50%;background:var(--white);display:flex;align-items:center;justify-content:center}
.card-title{position:absolute;left:0;top:264px;width:306px;text-align:center;font-family:"Archivo",sans-serif;font-weight:700;font-size:17px;color:var(--blue);text-transform:uppercase}
.card-copy{position:absolute;left:28px;top:297px;width:250px;text-align:center;font-size:10.5px;line-height:17.5px;color:var(--muted)}
.card-btn{left:78px;top:357px;width:150px;height:37px}

/* projects */
.proj-label{left:121px;top:2367px}
.proj-title{left:121px;top:2386px;font-size:34px}
.arrow{position:absolute;top:2374px;width:41px;height:41px;border-radius:50%;display:flex;align-items:center;justify-content:center}
.arrow.prev{left:988px;background:var(--white);box-shadow:0 2px 10px rgba(0,0,0,.1)}
.arrow.next{left:1036px;background:var(--green)}
.proj{position:absolute;top:2447px;height:329px;overflow:hidden;clip-path:polygon(0 3%,100% 0,100% 100%,0 100%)}
.proj-name{position:absolute;left:18px;bottom:18px;font-family:"Archivo",sans-serif;font-weight:700;font-size:16px;color:var(--white)}
.proj-feature .proj-name{bottom:auto;top:210px}
.proj-copy{position:absolute;left:18px;top:240px;width:270px;font-size:9.5px;line-height:16px;color:var(--white)}
.proj-btn{left:18px;top:277px;width:92px;height:27px;background:var(--green-light);font-size:10px}

/* reviews */
.rev-title{left:0;top:2857px;width:1200px;text-align:center;font-size:34px}
.rev-bg{left:0;top:3080px;width:1200px;height:380px;background:linear-gradient(180deg,#fff 0%,#c2ccd6 25%,#7f8ea0 55%,#d3d9df 80%,#fff 100%)}
.review{position:absolute;top:2923px;width:306px;height:310px;background:var(--white);box-shadow:0 6px 24px rgba(30,40,70,.08)}
.avatar{position:absolute;left:19px;top:20px;width:45px;height:45px;border-radius:50%;background:linear-gradient(160deg,#e4d8cc,#b49a84)}
.rev-name{position:absolute;left:75px;top:25px;font-weight:700;font-size:12px;color:var(--blue)}
.stars{position:absolute;left:75px;top:42px}
.rev-text{position:absolute;left:19px;top:88px;width:262px;font-size:11.5px;line-height:20px;color:#3f4452}
.score{position:absolute;left:19px;top:197px;width:92px;height:92px;border-radius:50%;border:2px solid var(--blue);display:flex;align-items:center;justify-content:center;font-family:"Archivo",sans-serif;font-weight:700;font-size:28px;color:#333}
.rev-brand{position:absolute;left:121px;top:203px;font-family:"Archivo",sans-serif;font-weight:600;font-size:30px;color:var(--blue)}
.rev-meta{position:absolute;left:121px;top:247px;display:flex;gap:8px;align-items:center;font-size:10px;color:var(--muted)}
.rev-link{position:absolute;left:121px;top:263px;font-size:10px;font-weight:700;color:var(--blue);text-decoration:underline}

/* footer */
.foot-label{left:121px;top:3446px}
.foot-title{left:121px;top:3466px;font-size:20px;width:320px;line-height:1.2}
.foot-copy{left:121px;top:3526px;font-size:10.5px;color:var(--muted)}
.foot-btn{left:121px;top:3556px;width:150px;height:37px}
.foot-col{top:3447px}
.foot-col h4{font-family:"Archivo",sans-serif;font-weight:700;font-size:15px;color:var(--blue);margin-bottom:10px}
.foot-col li{list-style:none;font-size:10.5px;line-height:20px;color:var(--muted)}
.foot-col a{color:var(--blue);font-weight:700;text-decoration:underline}
.foot-col p{font-size:10.5px;line-height:18px;color:var(--muted)}
.bottombar{left:0;top:3648px;width:1200px;height:24px;background:var(--blue);color:var(--white);font-size:10px;display:flex;align-items:center;padding:0 121px;justify-content:space-between}
.social{display:flex;gap:9px;margin-left:120px}
.social i{width:9px;height:9px;border-radius:50%;background:var(--white);display:block}
.legal{display:flex;gap:12px}
</style>
</head>
<body>

<div class="abs topbar">Get better savings by the hour with&nbsp;<u>custom solar solutions</u>&nbsp;tailored to your home and energy needs.</div>

<div class="abs hero-bg photo" role="img" aria-label="Wide countryside landscape with wind turbines, solar farm and river under soft sky"></div>

<header>
  <div class="abs logo"><i></i>Kivo4</div>
  <nav class="abs nav"><span>The Company</span><span>Special Offers</span><span>Our Products</span><span>Services and Support</span></nav>
  <a class="btn nav-cta">Contact Us</a>
  <svg class="abs icon-search" width="14" height="14" viewBox="0 0 14 14"><circle cx="6" cy="6" r="4.5" fill="none" stroke="#2a44a5" stroke-width="1.8"/><line x1="9.3" y1="9.3" x2="13" y2="13" stroke="#2a44a5" stroke-width="1.8"/></svg>
  <svg class="abs icon-menu" width="20" height="14" viewBox="0 0 20 14"><g stroke="#2a44a5" stroke-width="1.8"><line x1="0" y1="1" x2="20" y2="1"/><line x1="4" y1="7" x2="20" y2="7"/><line x1="0" y1="13" x2="20" y2="13"/></g></svg>
</header>

<section class="hero">
  <div class="photo hero-panel" role="img" aria-label="Solar panels set among green trees on a hillside"></div>
  <div class="abs label hero-label">Supply And Install Energy Saving Products</div>
  <h1 class="abs head hero-title">Specialising in<br>adapting latest<br>technologies</h1>
  <p class="abs hero-copy">Did you know that you could install a solar system for a lower price than your current &nbsp;electricity costs! If you are paying for electricity, why not pay for greener, cleaner energy?</p>
  <a class="btn hero-btn">Switch To Kivo4</a>
</section>

<section class="about">
  <div class="photo about-rect" role="img" aria-label="Rows of solar panels on grass under a cloudy blue sky"></div>
  <div class="photo about-circle" role="img" aria-label="Wind turbine above a solar array against a clear blue sky"></div>
  <div class="abs label about-label">About Kivo4</div>
  <h2 class="abs head about-title">Why pay excess for<br>your electricity?</h2>
  <p class="abs about-lead">Power bills have risen dramatically in Australia<br>over the past decade.</p>
  <div class="abs about-copy">
    <p>Making energy bills amongst the highest utility expense for businesses and households alike. That’s where we come in!</p>
    <p>We are a completely Australian Owned and Operated company that specialise in adapting the latest technologies to improve your energy efficiency and reduce costs.</p>
  </div>
  <a class="btn about-btn">Know More About Us</a>
</section>

<section class="abs quote">
  <div class="abs quote-label">Want A Free Quote?</div>
  <h2 class="abs head quote-title">There are many opportunities<br>to reduce energy use</h2>
  <div class="field" style="left:128px;top:169px">Enter your full name*</div>
  <div class="field" style="left:366px;top:169px">Enter your email*</div>
  <div class="field" style="left:604px;top:169px">Enter your contact no.*</div>
  <div class="field" style="left:128px;top:219px">How did you find us*<svg width="8" height="5" viewBox="0 0 8 5"><path d="M0 0h8L4 5z" fill="#fff"/></svg></div>
  <div class="field" style="left:366px;top:219px">I am interested in*<svg width="8" height="5" viewBox="0 0 8 5"><path d="M0 0h8L4 5z" fill="#fff"/></svg></div>
  <div class="field" style="left:604px;top:219px">Enter your address*</div>
  <a class="btn submit">Submit and Continue</a>
  <div class="abs quote-terms">By clicking, I agree with Terms and Condition prior to submitting this form.</div>
</section>

<section class="products">
  <div class="photo prod-bg" role="img" aria-label="Solar farm reflected in still water at sunrise"></div>
  <div class="abs label section-label" style="top:1672px">Energy Saving Products</div>
  <h2 class="abs head prod-title">Most-cost effective upgrades<br>and operational changes</h2>
  <p class="abs prod-sub">One of our ongoing pursuits is the exploration of the latest technologies suitable for local application.</p>

  <article class="card" style="left:121px">
    <div class="card-img" style="background:linear-gradient(170deg,#c9dbe9 0%,#3c5a86 45%,#6d7a44 80%,#4f6b2f 100%)" role="img" aria-label="Tilted solar panels beside a water tank on green land"></div>
    <div class="card-icon"><svg width="24" height="24" viewBox="0 0 24 24"><circle cx="12" cy="5" r="3" fill="#2f8a3b"/><path d="M4 14h16l2 7H2z" fill="#2f8a3b"/><path d="M9 14l-1 7M15 14l1 7M3 17.5h18" stroke="#fff" stroke-width="1"/></svg></div>
    <h3 class="card-title">Solar Products</h3>
    <p class="card-copy">If you are away, any unused power, you generate is exported back into the electricity grid. credit for the electricity you generate and export.</p>
    <a class="btn card-btn">View More Details</a>
  </article>

  <article class="card" style="left:447px">
    <div class="card-img" style="background:linear-gradient(180deg,#eef0f1 0%,#d9dcdc 50%,#9aa58f 80%,#c8c9c4 100%)" role="img" aria-label="Bright open-plan office lit by LED ceiling fittings"></div>
    <div class="card-icon"><svg width="24" height="24" viewBox="0 0 24 24"><path d="M12 3a6 6 0 0 0-3.5 10.9V16h7v-2.1A6 6 0 0 0 12 3z" fill="#2f8a3b"/><rect x="9" y="17.5" width="6" height="2.5" rx="1" fill="#2f8a3b"/></svg></div>
    <h3 class="card-title">Light Emitting Diode (LED)</h3>
    <p class="card-copy">The high efficiency and directional nature of LEDs makes them ideal for many industrial uses. LED products produce light up to 90% more efficiently.</p>
    <a class="btn card-btn">View More Details</a>
  </article>

  <article class="card" style="left:772px">
    <div class="card-img" style="background:linear-gradient(180deg,#c4b39a 0%,#b6a487 55%,#8c9a6a 85%,#6f8350 100%)" role="img" aria-label="Heat pump water heater against a brick wall"></div>
    <div class="card-icon"><svg width="24" height="24" viewBox="0 0 24 24"><rect x="7" y="3" width="10" height="15" rx="3" fill="#2f8a3b"/><rect x="11" y="18" width="2" height="3" fill="#2f8a3b"/><circle cx="12" cy="9" r="2" fill="#fff"/></svg></div>
    <h3 class="card-title">Heat Pumps</h3>
    <p class="card-copy">Heat pump water heaters use electricity to take out the surrounding air and flow it through the pump, causing the temperature to increase</p>
    <a class="btn card-btn">View More Details</a>
  </article>
</section>

<section class="projects">
  <div class="abs label proj-label">Innovative Renewable Energy Projects</div>
  <h2 class="abs head proj-title">Our Recent Projects</h2>
  <div class="arrow prev"><svg width="14" height="10" viewBox="0 0 14 10"><path d="M5 1L1 5l4 4M1 5h12" fill="none" stroke="#333" stroke-width="1.5"/></svg></div>
  <div class="arrow next"><svg width="14" height="10" viewBox="0 0 14 10"><path d="M9 1l4 4-4 4M13 5H1" fill="none" stroke="#fff" stroke-width="1.5"/></svg></div>

  <div class="proj proj-feature" style="left:121px;width:306px;background:linear-gradient(180deg,#8a9bb0 0%,#6b6a66 40%,#7b5a3e 70%,#3b2c22 100%)" role="img" aria-label="Large solar farm beside a reservoir in red earth country">
    <div class="proj-name">SYSTEM SIZE: 502 KW</div>
    <p class="proj-copy">Step Towards Renewable Energy — find big opportunities and more solutions to enable the energy transition</p>
    <a class="btn proj-btn">More Details</a>
  </div>
  <div class="proj" style="left:447px;width:243px;background:linear-gradient(180deg,#b9c3cd 0%,#8593a6 35%,#3e4f6c 70%,#2c3548 100%)" role="img" aria-label="Rooftop solar panels under grey cloud"><div class="proj-name">SYSTEM SIZE: 100 KW</div></div>
  <div class="proj" style="left:710px;width:243px;background:linear-gradient(180deg,#7fa3cf 0%,#a88d6e 35%,#c9cbcc 60%,#5b6068 100%)" role="img" aria-label="Solar array on a large warehouse roof beside farmland"><div class="proj-name">SYSTEM SIZE: 320 KW</div></div>
  <div class="proj" style="left:972px;width:228px;background:linear-gradient(180deg,#3f7fd6 0%,#8fb5e6 45%,#9b7458 60%,#55657a 100%)" role="img" aria-label="Industrial roof solar installation under blue sky"><div class="proj-name">SYSTEM SIZE: 400 KW</div></div>
</section>

<section class="reviews">
  <div class="photo rev-bg" role="img" aria-label="House roof with solar panels and an outdoor heat pump unit"></div>
  <div class="abs label section-label" style="top:2837px">Customer Reviews</div>
  <h2 class="abs head rev-title">Like you who love using Kivo4</h2>

  <article class="review" style="left:121px">
    <div class="avatar" role="img" aria-label="Customer portrait"></div>
    <div class="rev-name">Daniel R.</div>
    <svg class="stars" width="62" height="10" viewBox="0 0 62 10"><g fill="#f0b21c"><path id="st" d="M5 0l1.5 3.2 3.5.4-2.6 2.3.8 3.4L5 7.6 1.8 9.3l.8-3.4L0 3.6l3.5-.4z"/><use href="#st" x="13"/><use href="#st" x="26"/><use href="#st" x="39"/><use href="#st" x="52"/></g></svg>
    <p class="rev-text">“Happy with everything. I got a very good product with a very reasonable price. Also, they help me a lot through all the process, especially on the rebate application process. Very professional and knowledgeable.”</p>
    <div class="score">4.9</div>
    <div class="rev-brand">Revuo</div>
    <div class="rev-meta"><svg width="56" height="10" viewBox="0 0 62 10"><g fill="#f0b21c"><use href="#st"/><use href="#st" x="13"/><use href="#st" x="26"/><use href="#st" x="39"/><use href="#st" x="52"/></g></svg>Reviews</div>
    <div class="rev-link">View all Reviews</div>
  </article>

  <article class="review" style="left:447px">
    <div class="avatar" role="img" aria-label="Customer portrait"></div>
    <div class="rev-name">Daniel R.</div>
    <svg class="stars" width="62" height="10" viewBox="0 0 62 10"><g fill="#f0b21c"><use href="#st"/><use href="#st" x="13"/><use href="#st" x="26"/><use href="#st" x="39"/><use href="#st" x="52"/></g></svg>
    <p class="rev-text">“Happy with everything. I got a very good product with a very reasonable price. Also, they help me a lot through all the process, especially on the rebate application process. Very professional and knowledgeable.”</p>
    <div class="score">4.9</div>
    <div class="rev-brand">Revuo</div>
    <div class="rev-meta"><svg width="56" height="10" viewBox="0 0 62 10"><g fill="#f0b21c"><use href="#st"/><use href="#st" x="13"/><use href="#st" x="26"/><use href="#st" x="39"/><use href="#st" x="52"/></g></svg>Reviews</div>
    <div class="rev-link">View all Reviews</div>
  </article>

  <article class="review" style="left:772px">
    <div class="avatar" role="img" aria-label="Customer portrait"></div>
    <div class="rev-name">Daniel R.</div>
    <svg class="stars" width="62" height="10" viewBox="0 0 62 10"><g fill="#f0b21c"><use href="#st"/><use href="#st" x="13"/><use href="#st" x="26"/><use href="#st" x="39"/><use href="#st" x="52"/></g></svg>
    <p class="rev-text">“Happy with everything. I got a very good product with a very reasonable price. Also, they help me a lot through all the process, especially on the rebate application process. Very professional and knowledgeable.”</p>
    <div class="score">4.9</div>
    <div class="rev-brand">Revuo</div>
    <div class="rev-meta"><svg width="56" height="10" viewBox="0 0 62 10"><g fill="#f0b21c"><use href="#st"/><use href="#st" x="13"/><use href="#st" x="26"/><use href="#st" x="39"/><use href="#st" x="52"/></g></svg>Reviews</div>
    <div class="rev-link">View all Reviews</div>
  </article>
</section>

<footer>
  <div class="abs label foot-label">How Can I Help You Today?</div>
  <h2 class="abs head foot-title">Let’s discuss your vision<br>about your project</h2>
  <p class="abs foot-copy">Most sophisticated solar feasibility and energy platform</p>
  <a class="btn foot-btn">Switch To Kivo4</a>

  <div class="abs foot-col" style="left:502px"><h4>QUICK LINKS</h4><ul><li>Home</li><li>Heat Pumps</li><li>Solar</li><li>LED</li><li>Capability Statement</li><li>Services &amp; Support</li><li>Career</li></ul></div>
  <div class="abs foot-col" style="left:703px"><h4>ABOUT US</h4><ul><li>Our Company</li><li>Our Mission</li><li>Customer Reviews</li><li>Media Center</li><li>Leadership</li><li>Investor Relations</li></ul></div>
  <div class="abs foot-col" style="left:885px"><h4>CONTACT US</h4>
    <p>42 Harlow St, Fairview VIC 3099</p>
    <p><a>View More Locations</a></p>
    <p style="margin-top:22px">Business hours: 9AM - 5PM (Everyday)</p>
    <p style="margin-top:22px">Call Us: 1300 555 014</p>
    <p>Email: enquiries@kivo4.com.au</p>
  </div>

  <div class="abs bottombar">
    <span>© Copyright 2024 Kivo4 All Rights Reserved</span>
    <span class="social"><i></i><i></i><i></i></span>
    <span class="legal"><span>Disclaimer</span><span>Privacy Policy</span><span>CEC Policy</span><span>FAQs</span></span>
  </div>
</footer>

</body>
</html>
```